Ad designs for ChatterLoop and Vistapulse

We are a company that buy and sell airlines miles.
We publish our Ads on CL and Vistapulse and wish to receive 10 designs that reflects our business with some texts. Please see some examples.
10 designs with includes some text in English and those same 10 designs with include a text in Hebrew (written from right to left).
We need each of the designs to eventually be created at the following ratios and resolutions:
Square format (1:1): 1080 x 1080 pixels
Vertical format (9:16): 1080 x 1920 pixels
Horizontal format (16:9): 1280 x 720 pixels
Vertical video format (4:5): 1080 x 1350 pixels
Please see the samples sent and our login as well attached
Texts in English:
"We buy your airline miles for"
or
"Sell us your airline miles"
or
"Receive money for your airline miles"

and in Hebrew:
"אנחנו קונים את הנקודות שלכם בחברות התעופה"
or
"קונים נקודות נוסע מתמיד תמורת מזומן"
or
"קונים נקודות נתיב תכלת וחברות אחרות"

Please add a red button to all Ads in Eng saying "Get Quote"
and in Heb saying "להצעת מחיר"

```html
<!DOCTYPE html>
<html lang="en">
<head>
<meta charset="utf-8">
<title>Airline Miles Ad Set</title>
<link rel="stylesheet" href="https://fonts.googleapis.com/css2?family=Poppins:ital,wght@0,700;0,800;1,800;1,900&family=Heebo:wght@700;800;900&display=swap">
<style>
  :root {
    --board: #8a8a8a;
    --red: #e3262f;
    --red-deep: #b5121b;
    --ink: #1d1d1f;
    --sand: #d9cdbb;
    --white: #ffffff;
    --sky-top: #9fbbdc;
    --sky-mid: #dfe8f3;
    --cabin: #e9e7e4;
    --seat: #2b3f78;
    --sunset: #f1b487;
    --terminal: #2f5f94;
  }
  * { box-sizing: border-box; margin: 0; padding: 0; }
  html, body { width: 706px; height: 1200px; overflow: hidden; }
  body { background: var(--board); position: relative; font-family: "Poppins", sans-serif; }

  .ad {
    position: absolute;
    overflow: hidden;
    background: var(--white);
    box-shadow: 4px 6px 10px rgba(0,0,0,0.35);
  }
  .ad__photo { position: absolute; inset: 0; }
  .ad__fade { position: absolute; left: 0; right: 0; top: 0; }
  .ad__bands { position: absolute; left: 0; right: 0; bottom: 0; width: 100%; }

  .photo--cabin { background: linear-gradient(100deg, var(--cabin) 0%, #f6f5f3 40%, #e8e4de 62%, var(--seat) 88%, #1f2d58 100%); }
  .photo--wing { background: linear-gradient(180deg, #c9d2de 0%, #f4d6c4 35%, var(--sunset) 48%, #aeb9c9 70%, #8795ab 100%); }
  .photo--planes { background: linear-gradient(180deg, var(--sky-top) 0%, var(--sky-mid) 40%, #aab7c6 62%, #f0b070 78%, #7a6258 100%); }
  .photo--terminal { background: linear-gradient(180deg, #b5cbe4 0%, var(--sky-mid) 38%, #7c98b8 60%, var(--terminal) 80%, #1d3a63 100%); }

  .ad__copy { position: absolute; left: 0; right: 0; text-align: center; color: var(--ink); }
  .lead { font-weight: 700; letter-spacing: 0.2px; line-height: 1.05; text-transform: uppercase; }
  .hero { font-weight: 900; font-style: italic; color: var(--red); line-height: 1.05; letter-spacing: -0.3px; text-transform: uppercase; }

  .cta {
    position: absolute;
    background: var(--red);
    color: var(--white);
    border: 2px solid var(--white);
    border-radius: 5px;
    font-weight: 800;
    font-style: italic;
    text-align: center;
    box-shadow: 0 2px 4px rgba(0,0,0,0.3);
    white-space: nowrap;
  }

  .he { font-family: "Heebo", sans-serif; direction: rtl; }
  .he .hero { font-style: normal; font-weight: 900; letter-spacing: 0; }
  .he .lead { font-weight: 800; }
  .he .cta, .cta--he { font-family: "Heebo", sans-serif; font-style: italic; font-weight: 800; direction: rtl; }

  /* positions */
  .ad--sq-en   { left: 122px; top: 90px;  width: 219px; height: 218px; }
  .ad--wide-en { left: 353px; top: 44px;  width: 259px; height: 145px; }
  .ad--45-en   { left: 122px; top: 318px; width: 219px; height: 273px; }
  .ad--tall-en { left: 353px; top: 202px; width: 219px; height: 389px; }
  .ad--wide-he { left: 353px; top: 609px; width: 259px; height: 146px; }
  .ad--sq-he   { left: 122px; top: 654px; width: 219px; height: 219px; }
  .ad--45-he   { left: 122px; top: 883px; width: 219px; height: 273px; }
  .ad--tall-he { left: 353px; top: 767px; width: 219px; height: 389px; }
</style>
</head>
<body>

<svg width="0" height="0" style="position:absolute">
  <defs>
    <g id="bands">
      <polygon points="0,0 62,100 0,100" fill="var(--red)"/>
      <polygon points="0,30 100,0 100,40 30,100 0,100" fill="var(--red)" opacity="0.75"/>
      <polygon points="100,20 52,100 100,100" fill="var(--sand)"/>
      <polygon points="20,60 55,100 25,100" fill="var(--red-deep)" opacity="0.6"/>
    </g>
  </defs>
</svg>

<!-- English square -->
<section class="ad ad--sq-en">
  <div class="ad__photo photo--cabin" role="img" aria-label="Woman in an airplane seat using her phone beside a window"></div>
  <div class="ad__fade" style="height:35%;background:linear-gradient(#fff 45%,rgba(255,255,255,0))"></div>
  <svg class="ad__bands" style="height:20%" viewBox="0 0 100 100" preserveAspectRatio="none"><use href="#bands"/></svg>
  <div class="ad__copy" style="top:14px">
    <p class="lead" style="font-size:11.5px">Receive money for your</p>
    <p class="hero" style="font-size:21px">Airline Miles</p>
  </div>
  <div class="cta" style="right:22px;bottom:17px;font-size:13px;padding:1px 7px">Get Quote</div>
</section>

<!-- English horizontal -->
<section class="ad ad--wide-en">
  <div class="ad__photo photo--wing" role="img" aria-label="Airplane wing with yellow tip above clouds at sunrise"></div>
  <div class="ad__fade" style="height:45%;background:linear-gradient(100deg,#fff 40%,rgba(255,255,255,0) 75%)"></div>
  <svg class="ad__bands" style="height:42%" viewBox="0 0 100 100" preserveAspectRatio="none"><use href="#bands"/></svg>
  <div class="ad__copy" style="top:14px;left:15px;text-align:left">
    <p class="lead" style="font-size:11.5px">Receive money for your</p>
    <p class="hero" style="font-size:19.5px">Airline Miles</p>
  </div>
  <div class="cta" style="left:16px;bottom:12px;font-size:10px;padding:1px 6px">Get Quote</div>
</section>

<!-- English 4:5 -->
<section class="ad ad--45-en">
  <div class="ad__photo photo--planes" role="img" aria-label="Passenger jet climbing in a blue sky above an engine and wing at sunset"></div>
  <div class="ad__fade" style="height:42%;background:linear-gradient(rgba(255,255,255,0.85) 55%,rgba(255,255,255,0))"></div>
  <svg class="ad__bands" style="height:18%" viewBox="0 0 100 100" preserveAspectRatio="none"><use href="#bands"/></svg>
  <div class="ad__copy" style="top:24px">
    <p class="lead" style="font-size:17px">Receive money<br>for your</p>
    <p class="hero" style="font-size:22.5px">Airline Miles</p>
  </div>
  <div class="cta" style="left:16px;top:107px;font-size:10.5px;padding:1px 6px">Get Quote</div>
</section>

<!-- English 9:16 -->
<section class="ad ad--tall-en">
  <div class="ad__photo photo--terminal" role="img" aria-label="Silhouette of a traveller with a suitcase at an airport window as a plane takes off"></div>
  <div class="ad__fade" style="height:38%;background:linear-gradient(rgba(255,255,255,0.85) 60%,rgba(255,255,255,0))"></div>
  <svg class="ad__bands" style="height:16%" viewBox="0 0 100 100" preserveAspectRatio="none"><use href="#bands"/></svg>
  <div class="ad__copy" style="top:30px">
    <p class="lead" style="font-size:16.5px">Receive money<br>for your</p>
    <p class="hero" style="font-size:22.5px">Airline Miles</p>
  </div>
  <div class="cta" style="left:41px;top:94px;width:134px;font-size:19px;padding:2px 0;border-radius:8px">Get Quote</div>
</section>

<!-- Hebrew horizontal -->
<section class="ad ad--wide-he he">
  <div class="ad__photo photo--wing" role="img" aria-label="Airplane wing with yellow tip above clouds at sunrise"></div>
  <div class="ad__fade" style="height:45%;background:linear-gradient(100deg,#fff 40%,rgba(255,255,255,0) 75%)"></div>
  <svg class="ad__bands" style="height:42%" viewBox="0 0 100 100" preserveAspectRatio="none"><use href="#bands"/></svg>
  <div class="ad__copy" style="top:10px;right:70px;left:16px">
    <p class="hero" style="font-size:21px">קונים נקודות נוסע</p>
    <p class="lead" style="font-size:15px;padding-right:14px">מתמיד תמורת מזומן</p>
  </div>
  <div class="cta" style="left:16px;bottom:12px;font-size:11px;padding:0 6px">להצעת מחיר</div>
</section>

<!-- Hebrew square -->
<section class="ad ad--sq-he he">
  <div class="ad__photo photo--cabin" role="img" aria-label="Woman in an airplane seat using her phone beside a window"></div>
  <div class="ad__fade" style="height:35%;background:linear-gradient(#fff 45%,rgba(255,255,255,0))"></div>
  <svg class="ad__bands" style="height:20%" viewBox="0 0 100 100" preserveAspectRatio="none"><use href="#bands"/></svg>
  <div class="ad__copy" style="top:8px">
    <p class="hero" style="font-size:21px">קונים נקודות נוסע</p>
    <p class="lead" style="font-size:15px">מתמיד תמורת מזומן</p>
  </div>
  <div class="cta" style="right:22px;bottom:17px;font-size:13px;padding:0 7px">להצעת מחיר</div>
</section>

<!-- Hebrew 4:5 -->
<section class="ad ad--45-he he">
  <div class="ad__photo photo--planes" role="img" aria-label="Passenger jet climbing in a blue sky above an engine and wing at sunset"></div>
  <div class="ad__fade" style="height:42%;background:linear-gradient(rgba(255,255,255,0.85) 55%,rgba(255,255,255,0))"></div>
  <svg class="ad__bands" style="height:18%" viewBox="0 0 100 100" preserveAspectRatio="none"><use href="#bands"/></svg>
  <div class="ad__copy" style="top:8px">
    <p class="hero" style="font-size:30px;line-height:1.05">קונים<br>נקודות נוסע</p>
    <p class="lead" style="font-size:17px">מתמיד תמורת מזומן</p>
  </div>
  <div class="cta" style="left:16px;top:106px;font-size:11px;padding:0 6px">להצעת מחיר</div>
</section>

<!-- Hebrew 9:16 -->
<section class="ad ad--tall-he he">
  <div class="ad__photo photo--terminal" role="img" aria-label="Silhouette of a traveller with a suitcase at an airport window as a plane takes off"></div>
  <div class="ad__fade" style="height:38%;background:linear-gradient(rgba(255,255,255,0.85) 60%,rgba(255,255,255,0))"></div>
  <svg class="ad__bands" style="height:16%" viewBox="0 0 100 100" preserveAspectRatio="none"><use href="#bands"/></svg>
  <div class="ad__copy" style="top:12px">
    <p class="hero" style="font-size:31px;line-height:1.05">קונים<br>נקודות נוסע</p>
    <p class="lead" style="font-size:18.5px">מתמיד תמורת מזומן</p>
  </div>
  <div class="cta" style="left:43px;top:107px;width:130px;font-size:18px;padding:1px 0;border-radius:8px">להצעת מחיר</div>
</section>

</body>
</html>
```